80s style fun billboard for auto repair shop

A new design for our automotive shops’s advertisement billboard with an 80s-90s theme! Neon colors like photo example. Something eye catching but easy to read. Logos attached should be altered to match theme of advertisement. 1980s or 90s colors and theme. Details need to include an arrow and “1.2 miles ahead”, phone number “903-718-2249”, address “2856 W Tallow Ave”, and “best auto repair shop in town!” . Dimensions are 12'3"x 24'6"

Target Market(s)

Drive by attention

Industry/Entity Type

Automotive

Colors

Designer to choose colors to be used in the design.

Requirements
Must have
• My logo, address, phone number, tag line and badass 90s theme look!
Nice to have
• 80s color scheme, neon colors, use example photo for color ideas

```html
<!DOCTYPE html>
<html lang="en">
<head>
<meta charset="utf-8">
<title>Harlow's Premier Auto &amp; Diesel Billboard</title>
<link rel="stylesheet" href="https://fonts.googleapis.com/css2?family=Staatliches&family=Montserrat:wght@800;900&display=swap">
<style>
  :root {
    --page-bg: #c9c9c9;
    --board-blue: #1f7fd6;
    --ink: #1c1c1e;
    --car-navy: #163a66;
    --white: #ffffff;
    --yellow: #fff200;
    --mascot-red: #d8282d;
    --neon-pink: #ff2fb4;
    --neon-cyan: #3ff4ff;
  }
  * { margin: 0; padding: 0; box-sizing: border-box; }
  html, body { width: 967px; height: 1200px; overflow: hidden; }
  body { background: var(--page-bg); position: relative; }

  .billboard {
    position: absolute; left: 33px; top: 375px;
    width: 900px; height: 450px;
    background: var(--board-blue);
    box-shadow: 0 6px 14px rgba(0,0,0,.35);
    overflow: hidden;
  }
  .billboard > * { position: absolute; }

  .brand-mark {
    left: 46px; top: 40px;
    display: flex; align-items: center; gap: 8px;
    font-family: "Staatliches", sans-serif;
    font-size: 30px; line-height: 1; color: var(--white);
    white-space: nowrap;
  }
  .brand-mark .brand-square { width: 20px; height: 20px; background: var(--white); flex: none; }

  .car-art {
    left: 0; top: 144px; width: 369px; height: 190px;
    background: linear-gradient(180deg, var(--car-navy), var(--ink));
    border-radius: 60px 90px 20px 0;
    opacity: .85;
  }
  .mascot-art {
    left: 108px; top: 136px; width: 140px; height: 314px;
    background: linear-gradient(180deg, var(--ink) 0%, var(--ink) 55%, var(--mascot-red) 75%, var(--ink) 100%);
    border-radius: 64px 64px 10px 10px;
  }
  .cert-badge {
    left: 29px; top: 346px; width: 72px; height: 72px;
    border: 3px solid var(--white); border-radius: 50%;
  }

  .shop-name {
    left: 270px; top: 22px; width: 592px;
    font-family: "Staatliches", sans-serif;
    font-size: 118px; line-height: 1; letter-spacing: 3px;
    color: var(--white); text-align: center;
    text-shadow: 4px 4px 0 var(--neon-pink), 0 0 14px var(--neon-cyan);
  }
  .shop-tagline {
    left: 290px; top: 140px; width: 566px;
    font-family: "Montserrat", sans-serif; font-weight: 900;
    font-size: 38px; line-height: 1; color: var(--white); text-align: center;
    letter-spacing: .5px;
  }
  .repair-wrench { left: 391px; top: 188px; width: 410px; height: 92px; }
  .repair-label {
    left: 391px; top: 217px; width: 410px;
    font-family: "Staatliches", sans-serif;
    font-size: 34px; line-height: 1; letter-spacing: 6px;
    color: var(--neon-cyan); text-align: center;
    text-shadow: 0 0 8px var(--neon-cyan);
  }
  .phone {
    left: 360px; top: 286px; width: 475px;
    font-family: "Montserrat", sans-serif; font-weight: 900;
    font-size: 60px; line-height: 1; letter-spacing: -1px;
    color: var(--yellow); text-align: center;
    text-shadow: 3px 3px 0 var(--neon-pink), 0 0 12px rgba(255,242,0,.6);
  }
  .direction-arrow { left: 237px; top: 352px; width: 630px; height: 54px; }
  .directions {
    left: 250px; top: 364px; width: 560px;
    display: flex; align-items: center; justify-content: space-between;
    font-family: "Montserrat", sans-serif; font-weight: 800; line-height: 1;
  }
  .directions .address { color: var(--white); font-size: 22px; }
  .directions .divider { width: 2px; height: 26px; background: var(--white); }
  .directions .distance { color: var(--yellow); font-size: 26px; font-weight: 900; letter-spacing: 1px; }
  .slogan {
    left: 270px; top: 414px; width: 592px;
    font-family: "Montserrat", sans-serif; font-weight: 900;
    font-size: 22px; line-height: 1; letter-spacing: 1px;
    color: var(--neon-pink); text-align: center; text-transform: uppercase;
    text-shadow: 0 0 6px var(--neon-pink), 1px 1px 0 var(--ink);
  }
</style>
</head>
<body>
  <main class="billboard">
    <div class="brand-mark"><span class="brand-square"></span>Dex's Auto Lube</div>

    <div class="car-art" role="img" aria-label="Illustration of a classic coupe silhouette"></div>
    <div class="mascot-art" role="img" aria-label="Illustrated mechanic mascot holding a wrench and an oil can"></div>
    <div class="cert-badge"></div>

    <h1 class="shop-name">Harlow's</h1>
    <p class="shop-tagline">PREMIER AUTO &amp; DIESEL</p>

    <svg class="repair-wrench" viewBox="0 0 430 105" preserveAspectRatio="none" aria-hidden="true">
      <path fill="var(--ink)" d="M0 8 L48 0 L88 30 L342 30 L382 0 L430 8 L396 52 L430 97 L382 105 L342 75 L88 75 L48 105 L0 97 L34 52 Z"/>
    </svg>
    <p class="repair-label">Repair Shop</p>

    <p class="phone">903-718-2249</p>

    <svg class="direction-arrow" viewBox="0 0 630 54" aria-hidden="true">
      <path fill="var(--ink)" d="M0 11 L600 11 L600 0 L630 27 L600 54 L600 43 L0 43 Z"/>
    </svg>
    <div class="directions">
      <span class="address">2856 W TALLOW AVE</span>
      <span class="divider"></span>
      <span class="distance">1.2 MILES AHEAD</span>
    </div>

    <p class="slogan">Best auto repair shop in town!</p>
  </main>
</body>
</html>
```